Vantrelo App Homepage Design making customers feel in control of their spend

Hi,
We need a App Homepage design with a UI similar to the attached mock up on an Quorix 4. The app is intended to put customers in control of their usage and spend on their fixed phone, broadband, mobile, gas and electricity.

Please fee free to propose improvements to the background images, icons, colours, etc.

Any questions please let me know.

Thanks
Bertram

Target Market(s)

Consumer customers

Industry/Entity Type

Internet

Font styles to use
Sans Serif

Colors
3276b5
0255a3
85acd3
cfdeed
ffffff

Requirements
Must have
• Content in line with the guidelines in the attached mock up

```html
<!DOCTYPE html>
<html lang="en">
<head>
<meta charset="utf-8">
<title>Vantrelo App Homepage</title>
<link href="https://fonts.googleapis.com/css2?family=Source+Sans+3:wght@300;400;600;700&display=swap" rel="stylesheet">
<style>
  :root {
    --blue-mid: #3276b5;
    --blue-deep: #0255a3;
    --blue-soft: #85acd3;
    --blue-pale: #cfdeed;
    --white: #ffffff;
    --navy: #0b2a6e;
    --greet: #8aa9d4;
    --welcome: #7f9fce;
    --line: #c9c9c9;
    --menu: #b5b5b5;
    --gas: #b077d8;
    --mobile: #35c21a;
    --calls: #cf5a47;
    --fibre: #ccab48;
  }
  * { box-sizing: border-box; margin: 0; padding: 0; }
  html, body { width: 1200px; height: 878px; overflow: hidden; background: var(--white); }
  body { position: relative; font-family: "Source Sans 3", sans-serif; }

  .screen { position: absolute; top: 156px; width: 324px; height: 575px; overflow: hidden; }
  .screen--day { left: 66px; background: var(--white); border: 1px solid var(--line); }
  .screen--night { left: 491px; background: #000; }

  .menu { position: absolute; left: 13px; top: 11px; width: 26px; }
  .menu span { display: block; height: 3px; background: var(--menu); margin-bottom: 6px; }
  .screen--night .menu span { background: #8a8a8a; }

  .brand { position: absolute; top: 48px; left: 0; width: 100%; display: flex; justify-content: center; align-items: center; gap: 12px; }
  .brand__dot { width: 46px; height: 46px; border-radius: 50%; background: var(--blue-mid); }
  .brand__name { font-size: 36px; font-weight: 700; color: var(--navy); line-height: 1; letter-spacing: -0.5px; }
  .screen--night .brand__name { color: var(--blue-deep); }

  .greeting { position: absolute; top: 124px; width: 100%; text-align: center; font-size: 15px; font-weight: 300; color: var(--greet); }
  .welcome { position: absolute; top: 142px; width: 100%; text-align: center; font-size: 21px; font-weight: 400; color: var(--welcome); }
  .screen--night .welcome { color: #a9c3e6; }

  .support { position: absolute; left: 42px; top: 172px; width: 244px; height: 33px; border-radius: 6px; border: 1px solid #ececec; background: var(--white); display: flex; align-items: center; justify-content: center; font-size: 16px; font-weight: 300; color: var(--blue-deep); }
  .screen--night .support { left: 42px; border: none; }

  .chart { position: absolute; left: 50px; top: 222px; width: 220px; height: 220px; }
  .chart text { font-family: "Source Sans 3", sans-serif; font-size: 12px; font-weight: 600; text-anchor: middle; }

  .charges-label { position: absolute; top: 471px; width: 100%; text-align: center; font-size: 21px; font-weight: 300; color: var(--blue-soft); }
  .screen--night .charges-label { color: var(--white); }
  .charges-amount { position: absolute; top: 495px; width: 100%; text-align: center; font-size: 21px; font-weight: 600; color: var(--blue-deep); }
  .screen--night .charges-amount { color: var(--white); }

  .bill { position: absolute; left: 42px; top: 523px; width: 244px; height: 42px; border-radius: 6px; border: 1px solid #ececec; background: var(--white); display: flex; flex-direction: column; align-items: center; justify-content: center; font-size: 11.5px; font-weight: 300; color: var(--blue-deep); line-height: 1.3; }
  .screen--night .bill { border: none; }

  .palette { position: absolute; left: 992px; top: 834px; display: flex; gap: 7px; }
  .palette span { width: 36px; height: 44px; }
</style>
</head>
<body>

<section class="screen screen--day">
  <div class="menu"><span></span><span></span><span></span></div>
  <div class="brand"><span class="brand__dot"></span><span class="brand__name">Vantrelo</span></div>
  <p class="greeting">Good Morning Marisa !</p>
  <p class="welcome">Welcome to Vantrelo</p>
  <div class="support">Call 24 / 7 Support</div>
  <svg class="chart" viewBox="-110 -110 220 220" role="img" aria-label="Spend by service">
    <path d="M0 0 L0 -105 A105 105 0 0 1 101.7 26.1 Z" fill="var(--blue-deep)"/>
    <path d="M0 0 L101.7 26.1 A105 105 0 0 1 61.7 84.9 Z" fill="var(--gas)"/>
    <path d="M0 0 L61.7 84.9 A105 105 0 0 1 -61.7 84.9 Z" fill="var(--mobile)"/>
    <path d="M0 0 L-61.7 84.9 A105 105 0 0 1 -103.1 -19.7 Z" fill="var(--calls)"/>
    <path d="M0 0 L-103.1 -19.7 A105 105 0 0 1 0 -105 Z" fill="var(--fibre)"/>
    <g fill="#fff">
      <text x="55" y="-30">Electricity<tspan x="55" dy="15">(29%)</tspan></text>
      <text x="56" y="50">Gas<tspan x="56" dy="15">(11%)</tspan></text>
      <text x="-10" y="67">Mobile<tspan x="-10" dy="15">(20%)</tspan></text>
      <text x="-62" y="14">Calls<tspan x="-62" dy="15">(18%)</tspan></text>
      <text x="-48" y="-51">Fibre<tspan x="-48" dy="15">(22%)</tspan></text>
    </g>
  </svg>
  <p class="charges-label">Your current total charges</p>
  <p class="charges-amount">$ 68.39</p>
  <div class="bill"><span>Last Bill : $ 75.76 on 09 / 12 / 2016</span><span>Allowance renews in 18 days</span></div>
</section>

<section class="screen screen--night">
  <div class="menu"><span></span><span></span><span></span></div>
  <div class="brand"><span class="brand__dot"></span><span class="brand__name">Vantrelo</span></div>
  <p class="greeting">Good Evening Marisa !</p>
  <p class="welcome">Welcome to Vantrelo</p>
  <div class="support">Call 24 / 7 Support</div>
  <svg class="chart" viewBox="-110 -110 220 220" role="img" aria-label="Spend by service">
    <path d="M0 0 L0 -105 A105 105 0 0 1 101.7 26.1 Z" fill="var(--blue-pale)"/>
    <path d="M0 0 L101.7 26.1 A105 105 0 0 1 61.7 84.9 Z" fill="var(--blue-soft)"/>
    <path d="M0 0 L61.7 84.9 A105 105 0 0 1 -61.7 84.9 Z" fill="var(--blue-deep)"/>
    <path d="M0 0 L-61.7 84.9 A105 105 0 0 1 -103.1 -19.7 Z" fill="var(--blue-mid)"/>
    <path d="M0 0 L-103.1 -19.7 A105 105 0 0 1 0 -105 Z" fill="var(--white)"/>
    <g fill="#111">
      <text x="55" y="-30">Electricity<tspan x="55" dy="15">(29%)</tspan></text>
      <text x="56" y="50">Gas<tspan x="56" dy="15">(11%)</tspan></text>
      <text x="-10" y="67">Mobile<tspan x="-10" dy="15">(20%)</tspan></text>
      <text x="-62" y="14">Calls<tspan x="-62" dy="15">(18%)</tspan></text>
      <text x="-48" y="-51">Fibre<tspan x="-48" dy="15">(22%)</tspan></text>
    </g>
  </svg>
  <p class="charges-label">Your current total charges</p>
  <p class="charges-amount">$ 68.39</p>
  <div class="bill"><span>Last Bill : $ 75.76 on 09 / 12 / 2016</span><span>Allowance renews in 18 days</span></div>
</section>

<div class="palette" aria-label="Colour palette">
  <span style="background: var(--blue-mid)"></span>
  <span style="background: var(--blue-deep)"></span>
  <span style="background: var(--blue-soft)"></span>
  <span style="background: var(--blue-pale)"></span>
</div>

</body>
</html>
```